TRELUDAX.live*

I am needing a web site built for the main purpose of uploading podcasts
(MP3 files) to be viewed by large audiences of 1000+ site visitors on a regular basis. I have created a rough draft of how I want the site to look.

i have created a rough draft of the home page - the LOGO for this site is a spectacular lightening bolt which appears on my home page sample... the file for this image I purchased is too large to download to your site. I will supply on reuquest.

There will be 5 pages; HOME ABOUT RESOURCES DEVOTIONALS GLENN.
I have all the content prepared for each of the above pages.

Target Market(s)

All people groups seeking positive and encouraging words, life lessons and testimonies of faith.

Coding

Coded - Design and coding required

Number of Pages Required

1 page

Colors
3176b5

Requirements
Must have
• The design and layout provided - my sample

Black backgrounds as shown on my sample

```html
<!DOCTYPE html>
<html lang="en">
<head>
<meta charset="utf-8">
<title>TRELUDAX.live – Life Changing Podcasts</title>
<link href="https://fonts.googleapis.com/css2?family=Abril+Fatface&family=Bodoni+Moda:wght@700;800&family=Heebo:wght@400;500;700&display=swap" rel="stylesheet">
<style>
:root{
  --brand:#3176b5;
  --page:#050505;
  --card:#111111;
  --navy-deep:#020824;
  --navy:#0a1f6e;
  --white:#ffffff;
  --text-soft:#cfcfcf;
  --meta:#e6e6e6;
  --line:#ffffff;
}
*{margin:0;padding:0;box-sizing:border-box}
html,body{width:1200px;height:2626px;overflow:hidden;background:var(--page)}
body{position:relative;font-family:'Heebo',sans-serif;color:var(--white)}

/* ---------- hero ---------- */
.hero{position:absolute;left:0;top:0;width:1200px;height:584px;overflow:hidden}
.hero-art{position:absolute;inset:0;
  background:radial-gradient(ellipse 460px 380px at 470px 300px,#1248c8 0%,#0a2a9a 40%,rgba(4,14,70,0) 80%),
             linear-gradient(90deg,#03103f 0%,#061a7a 40%,#03124c 70%,var(--navy-deep) 100%);}
.hero-portrait{position:absolute;left:95px;top:95px;width:375px;height:489px;
  border-radius:170px 170px 0 0;
  background:linear-gradient(180deg,#b88f78 0%,#9c7563 28%,#222 45%,#161616 100%);}
.main-nav{position:absolute;left:0;top:0;width:1200px;height:82px}
.main-nav a{position:absolute;top:31px;transform:translateX(-50%);font-family:'Bodoni Moda',serif;font-weight:800;
  font-size:15px;letter-spacing:.3px;color:var(--white);text-decoration:none;text-transform:uppercase}
.brand{position:absolute;left:600px;top:12px;transform:translateX(-50%);font-family:'Abril Fatface',serif;
  font-size:46px;line-height:56px;color:var(--white);white-space:nowrap;letter-spacing:1px}
.hero-title{position:absolute;left:660px;top:168px;width:450px;text-align:center;font-family:'Abril Fatface',serif;
  font-size:72px;line-height:97px;letter-spacing:3px;text-transform:uppercase;font-weight:400}
.slider-dots{position:absolute;top:483px;left:776px;display:flex;gap:10px}
.slider-dots span{display:block;width:46px;height:2px;background:rgba(255,255,255,.3)}
.slider-dots span.is-active{background:var(--white);height:3px}

/* ---------- episodes ---------- */
.episodes-head{position:absolute;left:111px;top:662px}
.section-title{font-family:'Abril Fatface',serif;font-weight:400;font-size:31px;letter-spacing:2px;line-height:40px;text-transform:uppercase}
.section-lead{margin-top:8px;width:470px;font-size:14px;line-height:28px;color:var(--white)}
.episode{position:absolute;left:111px;width:978px;height:209px;background:var(--card);border-radius:2px}
.episode.is-playing{background:var(--brand)}
.episode-art{position:absolute;left:11px;top:9px;width:197px;height:192px}
.episode-title{position:absolute;left:237px;top:26px;font-size:19.5px;font-weight:700;letter-spacing:.2px;text-transform:uppercase}
.episode-meta{position:absolute;left:237px;top:62px;font-size:11px;color:var(--meta);text-transform:uppercase;word-spacing:1px}
.episode-meta span{margin:0 6px}
.episode-excerpt{position:absolute;left:237px;top:88px;width:720px;font-size:14px;line-height:27px;color:var(--text-soft)}
.episode.is-playing .episode-excerpt{color:var(--white)}
.player{position:absolute;left:0;top:152px;width:978px;height:40px;color:var(--brand)}
.episode.is-playing .player{color:var(--white)}
.player svg{position:absolute}
.player .time{position:absolute;top:13px;font-size:10px;color:#9a9a9a}
.episode.is-playing .player .time{color:var(--white)}
.player .track{position:absolute;left:376px;top:19px;width:359px;height:2px;background:var(--line)}
.player .vol-track{position:absolute;left:804px;top:19px;width:41px;height:2px;background:var(--brand)}
.episode.is-playing .vol-track{background:var(--white)}
.player .vol-knob{position:absolute;left:839px;top:15px;width:10px;height:10px;border-radius:50%;background:var(--white)}
.player .speed{position:absolute;left:852px;top:12px;width:29px;height:15px;border:1px solid var(--white);
  font-size:9px;line-height:13px;text-align:center;color:var(--white)}

.more-btn{position:absolute;left:498px;top:1924px;width:204px;height:55px;border-radius:28px;background:var(--brand);
  font-size:17px;font-weight:500;line-height:55px;text-align:center;color:var(--white);text-transform:uppercase;letter-spacing:.3px}

/* ---------- subscribe ---------- */
.subscribe{position:absolute;left:0;top:2068px;width:1200px;height:351px}
.subscribe-art{position:absolute;inset:0;background:linear-gradient(180deg,#203321 0%,#2d3d2a 30%,#3b4346 60%,#2a2f33 100%)}
.subscribe-title{position:absolute;top:82px;width:1200px;text-align:center;font-family:'Bodoni Moda',serif;font-weight:700;font-size:33px;letter-spacing:.5px}
.subscribe-text{position:absolute;top:128px;width:1200px;text-align:center;font-size:13.5px;line-height:28px}
.subscribe-form{position:absolute;left:327px;top:212px;width:546px;height:52px;border-radius:26px;overflow:hidden;display:flex}
.subscribe-input{flex:1;background:var(--white);color:#8a8a8a;font-size:13px;line-height:52px;padding-left:24px}
.subscribe-btn{width:135px;background:var(--brand);font-size:14px;font-weight:700;letter-spacing:1.5px;line-height:52px;text-align:center}

/* ---------- footer ---------- */
.social{position:absolute;top:2472px;left:535px;display:flex;gap:7px}
.social span{display:block;width:27px;height:27px;border:1.5px solid var(--white);border-radius:50%}
.footer-nav{position:absolute;top:2523px;width:1200px;display:flex;justify-content:center;gap:28px;
  font-family:'Bodoni Moda',serif;font-weight:800;font-size:14.5px;text-transform:uppercase}
.footer-nav .sep{font-family:'Heebo',sans-serif;font-weight:400}
.copyright{position:absolute;top:2570px;width:1200px;text-align:center;font-size:15px}
</style>
</head>
<body>

<svg width="0" height="0" style="position:absolute">
  <defs>
    <symbol id="ic-rew" viewBox="0 0 20 20"><path d="M10 3a7 7 0 1 1-7 7" fill="none" stroke="currentColor" stroke-width="1.6"/><path d="M10 0v6L6 3z" fill="currentColor"/><text x="10" y="14" font-size="7" text-anchor="middle" fill="currentColor" font-family="Heebo,sans-serif">10</text></symbol>
    <symbol id="ic-fwd" viewBox="0 0 20 20"><path d="M10 3a7 7 0 1 0 7 7" fill="none" stroke="currentColor" stroke-width="1.6"/><path d="M10 0v6l4-3z" fill="currentColor"/><text x="10" y="14" font-size="7" text-anchor="middle" fill="currentColor" font-family="Heebo,sans-serif">10</text></symbol>
    <symbol id="ic-play" viewBox="0 0 36 36"><circle cx="18" cy="18" r="16.5" fill="none" stroke="currentColor" stroke-width="2"/><path d="M14 11v14l11-7z" fill="currentColor"/></symbol>
    <symbol id="ic-vol" viewBox="0 0 16 16"><path d="M2 6h3l4-3v10l-4-3H2z" fill="currentColor"/><path d="M11 5a4 4 0 0 1 0 6M12.5 3a6.5 6.5 0 0 1 0 10" fill="none" stroke="currentColor" stroke-width="1.3"/></symbol>
    <symbol id="ic-ext" viewBox="0 0 16 16"><path d="M12 9v5H2V4h5" fill="none" stroke="#fff" stroke-width="1.6"/><path d="M9 1h6v6M15 1 7 9" fill="none" stroke="#fff" stroke-width="1.6"/></symbol>
    <symbol id="ic-dl" viewBox="0 0 18 14"><path d="M4.5 13a4 4 0 0 1-.5-8 5 5 0 0 1 9.5-1A4.5 4.5 0 0 1 14 13z" fill="#fff"/><path d="M9 5v5M6.5 8 9 10.5 11.5 8" fill="none" stroke="#111" stroke-width="1.5"/></symbol>
  </defs>
</svg>

<header class="hero">
  <div class="hero-art" role="img" aria-label="Deep blue background with a bright lightning bolt artwork"></div>
  <div class="hero-portrait" role="img" aria-label="Portrait of the host Glenn with arms crossed, wearing a black t-shirt"></div>
  <nav class="main-nav">
    <a href="#" style="left:152px">Home</a>
    <a href="#" style="left:253px">About</a>
    <a href="#" style="left:356px">Glenn</a>
    <a href="#" style="left:862px">Resources</a>
    <a href="#" style="left:1018px">Devotionals</a>
  </nav>
  <div class="brand">TRELUDAX.live</div>
  <h1 class="hero-title">Life<br>Changing<br>Podcasts</h1>
  <div class="slider-dots"><span class="is-active"></span><span></span><span></span><span></span></div>
</header>

<section class="episodes-head">
  <h2 class="section-title">Our Episodes</h2>
  <p class="section-lead">Sed velit sapien, commodo et dictum porta, varius id nibh. Vivamus sed sapien molestie maximus lorem ut commodo enim.</p>
</section>

<article class="episode" style="top:788px">
  <div class="episode-art" role="img" aria-label="Woman with open arms on a mountain deck at sunrise" style="background:linear-gradient(180deg,#2b8fa3 0%,#e0b84a 45%,#c79a3a 70%,#6a5a3e 100%)"></div>
  <h3 class="episode-title">Episode 01: The Future of Sed</h3>
  <p class="episode-meta">August 7, 2020<span>/</span>Admin<span>/</span>Life Changing<span>/</span>00:02:16<span>/</span>0 Comments</p>
  <p class="episode-excerpt">Lorem ipsum dolor sit amet, consectetur adipiscing elit, sed do eiusmod tempor incididunt ut labore et dolore magna aliqua. Quis ipsum suspendisse ultrices gravida...</p>
  <div class="player">
    <svg style="left:237px;top:11px" width="18" height="18"><use href="#ic-rew"/></svg>
    <svg style="left:262px;top:2px" width="36" height="36"><use href="#ic-play"/></svg>
    <svg style="left:307px;top:11px" width="18" height="18"><use href="#ic-fwd"/></svg>
    <span class="time" style="left:340px">00:00</span><span class="track"></span><span class="time" style="left:746px">00:00</span>
    <svg style="left:783px;top:12px" width="15" height="15"><use href="#ic-vol"/></svg>
    <span class="vol-track"></span><span class="vol-knob"></span><span class="speed">1x</span>
    <svg style="left:897px;top:12px" width="15" height="15"><use href="#ic-ext"/></svg>
    <svg style="left:921px;top:13px" width="18" height="14"><use href="#ic-dl"/></svg>
  </div>
</article>

<article class="episode" style="top:1011px">
  <div class="episode-art" role="img" aria-label="Man reading a glowing book beneath a large tree" style="background:linear-gradient(180deg,#4d6378 0%,#3c5266 40%,#2a3644 75%,#1b222b 100%)"></div>
  <h3 class="episode-title">Episode 02: The Future of Sed</h3>
  <p class="episode-meta">August 7, 2020<span>/</span>Admin<span>/</span>Life Changing<span>/</span>00:02:16<span>/</span>0 Comments</p>
  <p class="episode-excerpt">Lorem ipsum dolor sit amet, consectetur adipiscing elit, sed do eiusmod tempor incididunt ut labore et dolore magna aliqua. Quis ipsum suspendisse ultrices gravida...</p>
  <div class="player">
    <svg style="left:237px;top:11px" width="18" height="18"><use href="#ic-rew"/></svg>
    <svg style="left:262px;top:2px" width="36" height="36"><use href="#ic-play"/></svg>
    <svg style="left:307px;top:11px" width="18" height="18"><use href="#ic-fwd"/></svg>
    <span class="time" style="left:340px">00:00</span><span class="track"></span><span class="time" style="left:746px">00:00</span>
    <svg style="left:783px;top:12px" width="15" height="15"><use href="#ic-vol"/></svg>
    <span class="vol-track"></span><span class="vol-knob"></span><span class="speed">1x</span>
    <svg style="left:897px;top:12px" width="15" height="15"><use href="#ic-ext"/></svg>
    <svg style="left:921px;top:13px" width="18" height="14"><use href="#ic-dl"/></svg>
  </div>
</article>

<article class="episode is-playing" style="top:1234px">
  <div class="episode-art" role="img" aria-label="Silhouette walking a tightrope toward a cliff at sunset" style="background:linear-gradient(180deg,#f4a07a 0%,#f28a6a 45%,#e4503a 75%,#b52a22 100%)"></div>
  <h3 class="episode-title">Episode 03: The Future of Sed</h3>
  <p class="episode-meta">August 7, 2020<span>/</span>Admin<span>/</span>Life Changing<span>/</span>00:02:16<span>/</span>0 Comments</p>
  <p class="episode-excerpt">Lorem ipsum dolor sit amet, consectetur adipiscing elit, sed do eiusmod tempor incididunt ut labore et dolore magna aliqua. Quis ipsum suspendisse ultrices gravida...</p>
  <div class="player">
    <svg style="left:237px;top:11px" width="18" height="18"><use href="#ic-rew"/></svg>
    <svg style="left:262px;top:2px" width="36" height="36"><use href="#ic-play"/></svg>
    <svg style="left:307px;top:11px" width="18" height="18"><use href="#ic-fwd"/></svg>
    <span class="time" style="left:340px">00:00</span><span class="track"></span><span class="time" style="left:746px">00:00</span>
    <svg style="left:783px;top:12px" width="15" height="15"><use href="#ic-vol"/></svg>
    <span class="vol-track"></span><span class="vol-knob"></span><span class="speed">1x</span>
    <svg style="left:897px;top:12px" width="15" height="15"><use href="#ic-ext"/></svg>
    <svg style="left:921px;top:13px" width="18" height="14"><use href="#ic-dl"/></svg>
  </div>
</article>

<article class="episode" style="top:1457px">
  <div class="episode-art" role="img" aria-label="Coffee cup beside a note with a work-life balance word cloud" style="background:linear-gradient(135deg,#2f5d8a 0%,#5c7fa3 30%,#d9ccb2 55%,#bfae90 80%,#6f8fb0 100%)"></div>
  <h3 class="episode-title">Episode 04: The Future of Sed</h3>
  <p class="episode-meta">August 7, 2020<span>/</span>Admin<span>/</span>Life Changing<span>/</span>00:02:16<span>/</span>0 Comments</p>
  <p class="episode-excerpt">Lorem ipsum dolor sit amet, consectetur adipiscing elit, sed do eiusmod tempor incididunt ut labore et dolore magna aliqua. Quis ipsum suspendisse ultrices gravida...</p>
  <div class="player">
    <svg style="left:237px;top:11px" width="18" height="18"><use href="#ic-rew"/></svg>
    <svg style="left:262px;top:2px" width="36" height="36"><use href="#ic-play"/></svg>
    <svg style="left:307px;top:11px" width="18" height="18"><use href="#ic-fwd"/></svg>
    <span class="time" style="left:340px">00:00</span><span class="track"></span><span class="time" style="left:746px">00:00</span>
    <svg style="left:783px;top:12px" width="15" height="15"><use href="#ic-vol"/></svg>
    <span class="vol-track"></span><span class="vol-knob"></span><span class="speed">1x</span>
    <svg style="left:897px;top:12px" width="15" height="15"><use href="#ic-ext"/></svg>
    <svg style="left:921px;top:13px" width="18" height="14"><use href="#ic-dl"/></svg>
  </div>
</article>

<article class="episode" style="top:1680px">
  <div class="episode-art" role="img" aria-label="Motivational quote poster over a lake at dusk" style="background:linear-gradient(180deg,#6f9ac4 0%,#b7c9d9 40%,#5a6d80 70%,#1f2a36 100%)"></div>
  <h3 class="episode-title">Episode 05: The Future of Sed</h3>
  <p class="episode-meta">August 7, 2020<span>/</span>Admin<span>/</span>Life Changing<span>/</span>00:02:16<span>/</span>0 Comments</p>
  <p class="episode-excerpt">Lorem ipsum dolor sit amet, consectetur adipiscing elit, sed do eiusmod tempor incididunt ut labore et dolore magna aliqua. Quis ipsum suspendisse ultrices gravida...</p>
  <div class="player">
    <svg style="left:237px;top:11px" width="18" height="18"><use href="#ic-rew"/></svg>
    <svg style="left:262px;top:2px" width="36" height="36"><use href="#ic-play"/></svg>
    <svg style="left:307px;top:11px" width="18" height="18"><use href="#ic-fwd"/></svg>
    <span class="time" style="left:340px">00:00</span><span class="track"></span><span class="time" style="left:746px">00:00</span>
    <svg style="left:783px;top:12px" width="15" height="15"><use href="#ic-vol"/></svg>
    <span class="vol-track"></span><span class="vol-knob"></span><span class="speed">1x</span>
    <svg style="left:897px;top:12px" width="15" height="15"><use href="#ic-ext"/></svg>
    <svg style="left:921px;top:13px" width="18" height="14"><use href="#ic-dl"/></svg>
  </div>
</article>

<a class="more-btn">More Episodes</a>

<section class="subscribe">
  <div class="subscribe-art" role="img" aria-label="Forest road stretching into the distance"></div>
  <h2 class="subscribe-title">Subscribe to Our Mailing List</h2>
  <p class="subscribe-text">To receive ongoing updates and notifications on new episodes, please sign up to our<br>Newsletter and we'll make sure to keep you in the loop!</p>
  <div class="subscribe-form">
    <div class="subscribe-input">Your Email</div>
    <div class="subscribe-btn">SUBSCRIBE</div>
  </div>
</section>

<footer>
  <div class="social"><span></span><span></span><span></span><span></span></div>
  <nav class="footer-nav">
    <span>Home</span><span class="sep">|</span><span>About&nbsp;&nbsp; Glenn</span><span class="sep">|</span><span>Resources</span><span class="sep">|</span><span>Devotionals</span>
  </nav>
  <p class="copyright">Copyright © 2020 TRELUDAX.live. All Rights Reserved.</p>
</footer>

</body>
</html>
```